Audio and Video download site

I am looking for a good and beautiful website where users can be a able to download and upload musicial files and video file. Basically, there will be two categories. The first category for the music files( mp3, mva and other popular music files) while the second category will be for video files (mp4, wmv, divx and other files) users would be able to like and dislike a song/video. Users do not necessarily have to sign up for them to make you or download and upload files from the website. The website should be youthful.

```html
<!DOCTYPE html>
<html lang="en">
<head>
<meta charset="utf-8">
<title>VIBRA – Music &amp; Video</title>
<link href="https://fonts.googleapis.com/css2?family=Open+Sans:wght@400;600;700&family=Oswald:wght@700&display=swap" rel="stylesheet">
<style>
:root{
  --red:#f24e2a;
  --red-dark:#d93f1d;
  --ink:#222;
  --dark:#1b1b1b;
  --text:#555;
  --muted:#8a8f96;
  --page:#f3f5f8;
  --line:#e2e5ea;
  --white:#fff;
}
*{box-sizing:border-box;margin:0;padding:0}
html,body{width:1200px;height:2394px;overflow:hidden}
body{position:relative;background:var(--page);font-family:"Open Sans",Arial,sans-serif;color:var(--text)}
.abs{position:absolute}

/* header */
.site-header{left:0;top:0;width:1200px;height:120px;background:var(--white)}
.brand{left:99px;top:38px;display:flex;align-items:center;gap:10px}
.brand-mark{width:48px;height:48px;border-radius:50%;background:var(--red)}
.brand-name{font-weight:700;font-size:27px;color:var(--ink)}
.search{left:570px;top:43px;width:320px;height:36px;border:1px solid #ddd;border-radius:18px;background:#fff;overflow:hidden}
.search span{position:absolute;left:18px;top:10px;font-size:10px;font-style:italic;color:#aaa}
.search-btn{position:absolute;right:0;top:0;width:46px;height:36px;background:var(--red)}
.account{left:912px;top:52px;display:flex;gap:16px;font-size:10.5px;color:#444;text-transform:uppercase}
.account i{display:inline-block;width:10px;height:10px;background:var(--red);border-radius:2px;margin-right:6px;vertical-align:-1px}

.main-nav{left:0;top:120px;width:1200px;height:60px;background:var(--white);border-top:1px solid var(--line)}
.main-nav ul{list-style:none;display:flex;position:absolute;left:99px;top:0;width:1002px;height:60px}
.main-nav li{flex:1;text-align:center;line-height:60px;font-size:12px;color:#333;text-transform:uppercase}
.main-nav li.active{color:var(--red);border-top:6px solid var(--red);line-height:48px}

/* hero */
.hero{left:0;top:180px;width:1200px;height:478px;background:linear-gradient(100deg,#b9cdd2 0%,#d6e1e2 40%,#e8ecec 60%,#c7d4d6 100%)}
.hero-photo{position:absolute;left:640px;top:0;width:500px;height:478px;background:linear-gradient(160deg,#8b5f4a 0%,#d8b09a 35%,#4a9bd8 75%,#2f7fc1 100%);opacity:.55;border-radius:200px 0 0 0}
.hero-title{position:absolute;left:99px;top:130px;font-family:"Oswald",Impact,sans-serif;font-size:46px;color:#fff;text-shadow:2px 2px 4px rgba(0,0,0,.35);letter-spacing:.5px}
.hero-text{position:absolute;left:99px;top:200px;width:520px;font-size:13px;line-height:26px;color:#222;text-transform:uppercase}
.hero-actions{position:absolute;left:99px;top:266px;display:flex;gap:9px}
.btn-pill{height:46px;width:178px;border-radius:23px;font-size:11.5px;font-weight:700;color:#fff;text-align:center;line-height:46px;text-transform:uppercase}
.btn-red{background:var(--red)}
.btn-dark{background:var(--dark)}
.hero-dots{position:absolute;left:99px;top:432px;display:flex;gap:10px}
.hero-dots span{width:14px;height:14px;border-radius:50%;background:rgba(255,255,255,.6)}
.hero-dots span.on{background:var(--red)}

/* player */
.player{left:0;top:658px;width:1200px;height:87px;background:var(--dark)}
.player-label{position:absolute;left:0;top:0;width:235px;height:87px;background:var(--red);color:#fff;font-size:13px;font-weight:700;line-height:87px;padding-left:99px;text-transform:uppercase;white-space:nowrap}
.player-label svg{position:absolute;right:-35px;top:0}
.player-track{position:absolute;left:303px;top:18px;font-size:12px;color:#aaa}
.player-track em{font-style:normal;color:#666}
.player-bar{position:absolute;left:303px;top:48px;width:780px;height:20px}

/* section heads */
.section-title{font-size:21px;color:#333;text-transform:uppercase;display:flex;align-items:center;gap:10px;width:694px;border-bottom:1px solid var(--line);padding-bottom:6px}
.section-title b{font-weight:400}
.section-title i{display:block;width:66px;height:3px;background:var(--red)}
.tabs{display:flex;width:694px;height:54px;background:linear-gradient(#3a3a3a,#1d1d1d)}
.tabs span{position:relative;text-align:center;line-height:54px;font-size:13px;color:#eee;text-transform:uppercase;border-right:1px solid #444}
.tabs span.on{background:var(--red)}
.tabs span.on::after{content:"";position:absolute;left:50%;bottom:-9px;margin-left:-9px;border:9px solid transparent;border-bottom:0;border-top-color:var(--red)}

/* cards */
.card-grid{display:grid;grid-template-columns:repeat(3,216px);column-gap:23px;row-gap:26px}
.track-card{height:280px;background:#fff;border:1px solid #e6e8eb}
.track-photo{height:160px}
.track-body{padding:14px 10px 0}
.track-title{font-size:12.5px;font-weight:600;color:var(--red)}
.track-artist{font-size:10.5px;color:#444;margin-top:6px}
.track-artist i,.video-meta i{display:inline-block;width:9px;height:10px;background:var(--red);border-radius:0 0 4px 4px;margin-right:6px}
.votes{display:flex;gap:5px;margin-top:14px}
.vote{height:26px;padding:0 8px;font-size:10px;color:#fff;line-height:26px;white-space:nowrap}
.vote-like{background:var(--red);width:95px}
.vote-dislike{background:var(--dark);width:95px}
.vote::before{content:"";display:inline-block;width:8px;height:8px;border:1.5px solid #fff;border-radius:2px;margin-right:5px;vertical-align:-1px}

/* video */
.video-stage{left:99px;top:1647px;width:694px;height:364px;background:linear-gradient(120deg,#3b332c 0%,#6f5a4a 40%,#b2927a 60%,#4a3f37 100%)}
.play-ring{position:absolute;left:50%;top:50%;width:96px;height:96px;margin:-48px 0 0 -48px;border:2px solid rgba(255,255,255,.8);border-radius:50%}
.play-ring::after{content:"";position:absolute;left:37px;top:28px;border-left:30px solid rgba(255,255,255,.85);border-top:19px solid transparent;border-bottom:19px solid transparent}
.video-title{left:99px;top:2027px;width:694px;font-size:13px;font-weight:600;color:var(--red);line-height:22px}
.video-meta{left:99px;top:2086px;display:flex;gap:6px;align-items:center;font-size:10.5px;color:#444}
.video-meta i{border-radius:1px}
.video-copy{left:99px;top:2122px;width:694px;font-size:11px;line-height:21px;color:#666}

/* sidebar */
.promo{left:825px;width:276px}
.promo-art{width:276px}
.promo-actions{display:flex;height:48px}
.promo-actions span{flex:1;font-size:10px;font-weight:700;color:#fff;line-height:48px;padding-left:10px;text-transform:uppercase}
.promo-actions span:first-child{background:var(--dark)}
.promo-actions span:last-child{background:var(--red)}
.social-box{left:825px;top:1583px;width:276px;height:117px;background:#e4e6e9;text-align:center}
.social-box h3,.side-title{font-size:15px;font-weight:400;color:var(--red);text-transform:uppercase}
.social-box h3{margin-top:22px}
.share-row{display:flex;justify-content:center;gap:8px;margin-top:14px}
.share{width:41px}
.share b{display:block;height:20px;font-size:9px;color:#fff;line-height:20px;font-weight:400}
.share span{display:block;height:20px;background:#fff;border:1px solid #ccc;font-size:9px;line-height:18px;color:#333}
.side-title{left:825px;width:276px;text-align:center}
.featured{left:827px;top:1776px;width:272px;height:158px;background:linear-gradient(#cfe2e8,#e8eee9 60%,#d9cbb0)}
.featured .dot{position:absolute;left:116px;top:59px;width:40px;height:40px;border-radius:50%;background:rgba(255,255,255,.8)}
.featured .dot::after{content:"";position:absolute;left:15px;top:11px;border-left:14px solid #333;border-top:9px solid transparent;border-bottom:9px solid transparent}
.thumbs{left:827px;top:1950px;display:flex;gap:12px}
.thumbs span{width:82px;height:46px;background:linear-gradient(#6a7d8c,#9a8670)}
.field{left:825px;width:276px;height:38px;background:#fff;border:1px solid #e4e4e4;font-size:10px;color:#aaa;padding:12px 14px}
.send{left:825px;top:2170px;width:108px;height:40px;background:var(--red);color:#fff;font-size:12px;font-weight:700;text-align:center;line-height:40px}
.remember{left:957px;top:2172px;font-size:10.5px;color:#777;line-height:22px}
.remember i{display:inline-block;width:12px;height:12px;border:1px solid #ccc;margin-right:8px;vertical-align:-2px}

/* footer */
.site-footer{left:0;top:2255px;width:1200px;height:139px;background:#0c0c0c;border-top:4px solid var(--red)}
.partners{position:absolute;left:116px;top:28px;display:flex;gap:26px;align-items:center}
.partners span{height:18px;background:#cfcfcf;border-radius:3px}
.footer-line{position:absolute;left:116px;top:66px;width:968px;height:1px;background:#2a2a2a}
.footer-links{position:absolute;left:0;top:80px;width:1200px;text-align:center;font-size:10px;color:#bbb;text-transform:uppercase;word-spacing:2px}
.copyright{position:absolute;left:0;top:102px;width:1200px;text-align:center;font-size:9.5px;color:#999;text-transform:uppercase}
.page-code{position:absolute;right:26px;top:100px;font-size:10px;color:#888}
</style>
</head>
<body>

<header class="site-header abs">
  <div class="brand abs"><span class="brand-mark"></span><span class="brand-name">VIBRA</span></div>
  <div class="search abs"><span>Search here...</span><div class="search-btn"><svg width="46" height="36"><circle cx="22" cy="17" r="5" fill="none" stroke="#fff" stroke-width="2"/><line x1="26" y1="21" x2="29" y2="24" stroke="#fff" stroke-width="2"/></svg></div></div>
  <div class="account abs"><span><i></i>My Account</span><span><i></i>Check Out</span></div>
</header>

<nav class="main-nav abs">
  <ul><li class="active">Home</li><li>Artists</li><li>Releases</li><li>Songs</li><li>Videos</li><li>Gallery</li><li>Contact</li></ul>
</nav>

<section class="hero abs">
  <div class="hero-photo" role="img" aria-label="Young woman with headphones enjoying music"></div>
  <h1 class="hero-title">NEMO ENIM IPSAM VOLUP</h1>
  <p class="hero-text">Sed ut perspiciatis unde omnis iste natus error sit voluptatem tium doloremque laudantium, totam rem aperiam...</p>
  <div class="hero-actions"><span class="btn-pill btn-red">Click view more</span><span class="btn-pill btn-dark">Get start today</span></div>
  <div class="hero-dots"><span class="on"></span><span></span><span></span></div>
</section>

<section class="player abs">
  <div class="player-label">Recent hit music<svg width="36" height="87"><polygon points="0,0 36,43.5 0,87" fill="#f24e2a"/></svg></div>
  <div class="player-track">Sed ut perspiciatis unde omnis iste natus error sit voluptatem accusantiu <em>(5:40/1:06)</em></div>
  <svg class="player-bar" viewBox="0 0 780 20">
    <polygon points="0,10 7,5 7,15" fill="#888"/><polygon points="20,2 34,10 20,18" fill="#aaa"/><polygon points="48,5 55,10 48,15" fill="#888"/>
    <rect x="66" y="5" width="9" height="2" fill="#888"/><rect x="66" y="9" width="9" height="2" fill="#888"/><rect x="66" y="13" width="9" height="2" fill="#888"/>
    <rect x="96" y="8" width="560" height="4" fill="#333"/><rect x="96" y="8" width="40" height="4" fill="#666"/>
    <polygon points="675,8 679,8 683,5 683,15 679,12 675,12" fill="#888"/>
    <rect x="693" y="8" width="80" height="4" fill="#333"/><rect x="693" y="8" width="28" height="4" fill="#888"/>
  </svg>
</section>

<!-- music category -->
<h2 class="section-title abs" style="left:99px;top:782px"><b>Music Category</b><i></i></h2>
<div class="tabs abs" style="left:99px;top:829px">
  <span class="on" style="width:188px">MP3</span><span style="width:217px">MVA</span><span style="width:289px;border:0">Popular Music Files</span>
</div>
<div class="card-grid abs" style="left:99px;top:909px">
  <article class="track-card"><div class="track-photo" role="img" aria-label="Blonde singer with vintage microphone" style="background:linear-gradient(135deg,#e9d6b8,#5a4a3a)"></div><div class="track-body"><div class="track-title">Accusantium Doloremque</div><div class="track-artist"><i></i>-LoopNorth Funky</div><div class="votes"><span class="vote vote-like">Likes:12,536</span><span class="vote vote-dislike">DisLikes:124</span></div></div></article>
  <article class="track-card"><div class="track-photo" role="img" aria-label="Singer in gold outfit with microphone" style="background:linear-gradient(135deg,#2a1c14,#8a6a3a)"></div><div class="track-body"><div class="track-title">Accusantium Doloremque</div><div class="track-artist"><i></i>-LoopNorth Funky</div><div class="votes"><span class="vote vote-like">Likes:12,536</span><span class="vote vote-dislike">DisLikes:124</span></div></div></article>
  <article class="track-card"><div class="track-photo" role="img" aria-label="Female vocalist singing on stage" style="background:linear-gradient(135deg,#6a6aa8,#c8c8e0)"></div><div class="track-body"><div class="track-title">Accusantium Doloremque</div><div class="track-artist"><i></i>-LoopNorth Funky</div><div class="votes"><span class="vote vote-like">Likes:12,536</span><span class="vote vote-dislike">DisLikes:124</span></div></div></article>
  <article class="track-card"><div class="track-photo" role="img" aria-label="Male singer at studio microphone" style="background:linear-gradient(135deg,#2f8fa8,#1c2c3a)"></div><div class="track-body"><div class="track-title">Accusantium Doloremque</div><div class="track-artist"><i></i>-LoopNorth Funky</div><div class="votes"><span class="vote vote-like">Likes:12,536</span><span class="vote vote-dislike">DisLikes:124</span></div></div></article>
  <article class="track-card"><div class="track-photo" role="img" aria-label="Guitarist singing against yellow backdrop" style="background:linear-gradient(135deg,#f4c21a,#b8860b)"></div><div class="track-body"><div class="track-title">Accusantium Doloremque</div><div class="track-artist"><i></i>-LoopNorth Funky</div><div class="votes"><span class="vote vote-like">Likes:12,536</span><span class="vote vote-dislike">DisLikes:124</span></div></div></article>
  <article class="track-card"><div class="track-photo" role="img" aria-label="Musician with acoustic guitar in studio" style="background:linear-gradient(135deg,#3f7fc8,#1a3a6a)"></div><div class="track-body"><div class="track-title">Accusantium Doloremque</div><div class="track-artist"><i></i>-LoopNorth Funky</div><div class="votes"><span class="vote vote-like">Likes:12,536</span><span class="vote vote-dislike">DisLikes:124</span></div></div></article>
</div>

<!-- video category -->
<h2 class="section-title abs" style="left:99px;top:1519px"><b>Video Category</b><i></i></h2>
<div class="tabs abs" style="left:99px;top:1566px">
  <span class="on" style="width:171px">MP4</span><span style="width:163px">WMV</span><span style="width:164px">DIVX</span><span style="width:196px;border:0">Other Files</span>
</div>
<div class="video-stage abs" role="img" aria-label="Young couple smiling on a city street"><span class="play-ring"></span></div>
<p class="video-title abs">Sed ut perspiciatis unde omnis iste natus error sit voluptatem accusantium doloremque laudantium, totam rem aperiam, eaque ipsa quae ab illo inventore veritatis et quasi architecto beatae vitae dicta...</p>
<div class="video-meta abs"><i></i>-LoopNorth Funky <span class="vote vote-like">Likes:12,536</span><span class="vote vote-dislike">DisLikes:124</span></div>
<p class="video-copy abs">In elementum pellentesque dolor ac gravida. Pellentesque elit leo, accumsan sed consectetur a, semper ac sem. Morbi sodales bibendum risus nec laoreet. Mauris est nisi, consequat vitae porta et, hendrerit sed metus.Aliquam eu magna vel metus ultrices ornare in et nisi. Quisque porta sodales orci, eu auctor leo tincidunt nec. Suspendisse posuere blandit tortor sit amet varius. Integer condimentum rutrum mi quis lobortis. Etiam consectetur posuere pretium...</p>

<!-- sidebar -->
<aside>
  <div class="promo abs" style="top:788px">
    <div class="promo-art" role="img" aria-label="Flowing music notes illustration" style="height:322px;background:linear-gradient(135deg,#fafafa,#e6e6e6)"></div>
    <div class="promo-actions"><span>Upload Music</span><span>Upload Videos</span></div>
  </div>
  <div class="promo abs" style="top:1186px">
    <div class="promo-art" role="img" aria-label="Male singer performing with microphone" style="height:320px;background:linear-gradient(160deg,#5a5a5a,#141414)"></div>
    <div class="promo-actions"><span>Download Music</span><span>Download Videos</span></div>
  </div>
  <div class="social-box abs">
    <h3>Social Media Links</h3>
    <div class="share-row">
      <div class="share"><b style="background:#3b5998">Like</b><span>24</span></div>
      <div class="share"><b style="background:#3ea9dd">Post</b><span>253</span></div>
      <div class="share"><b style="background:#c8232c">Pin</b><span>452</span></div>
      <div class="share"><b style="background:#6aa52a">Email</b><span>56</span></div>
      <div class="share"><b style="background:#444">Share</b><span>112</span></div>
    </div>
  </div>
  <h3 class="side-title abs" style="top:1732px">Featured Videos</h3>
  <div class="featured abs" role="img" aria-label="Father swinging child on a beach"><span class="dot"></span></div>
  <div class="thumbs abs"><span role="img" aria-label="Video thumbnail"></span><span role="img" aria-label="Video thumbnail"></span><span role="img" aria-label="Video thumbnail"></span></div>
  <h3 class="side-title abs" style="top:2038px;text-align:left">Users Log In</h3>
  <div class="field abs" style="top:2070px">User Name</div>
  <div class="field abs" style="top:2118px;color:#999;letter-spacing:3px">●●●●●</div>
  <div class="send abs">SEND</div>
  <div class="remember abs"><i></i>Remember Me<br>Lost Your Password??</div>
</aside>

<footer class="site-footer abs">
  <div class="partners">
    <span style="width:52px"></span><span style="width:74px"></span><span style="width:52px"></span><span style="width:72px"></span><span style="width:34px"></span><span style="width:104px"></span><span style="width:38px"></span><span style="width:62px"></span><span style="width:78px"></span><span style="width:66px"></span><span style="width:68px"></span>
  </div>
  <div class="footer-line"></div>
  <div class="footer-links">Home | Artists | Releases | Songs | Videos | Gallery | Contact</div>
  <div class="copyright">Copyrights©VIBRA .2016 | All rights reserved.</div>
  <div class="page-code">C11</div>
</footer>

</body>
</html>
```